Lead Generating Website Design

We are looking for a brand new design for our existing website.
The existing website is www.brvpartnerhub.com
The website is aimed at businesses that would like to licence the courses from our school to sell themselves.
We want the menu to be the following:
* Home
* About us
* Our Courses
* LMS Platform
* Affiliate Program
* Contact Us
We want the colour scheme to use the following design guide:
https://docvault.example/pedalforward/docs/keen_to_cycle_brand_guidelines
Like the idea of the circles and colours in the style guide for places. Want lots of white areas as well as coloured areas
An example of a nice looking site is : https://www.studyharbour.online/
MUST look good on mobile also
On the home page we want the following:
A large image with the text :
Over 450 courses written by highly qualified academics with real world experience.
The 'Join our thriving group of Affiliates - start your own online college!' section on the current website with the text and becoming an affiliate video
A section for 'see how our LMS works' with some text and a place for a video
A section for 'About BRV Remote Learning' with the text BRV Remote Learning has been providing distance education for over 40 years and have been the leader in online education for over 25 years.
Benefit from the resources and experience of one of the worlds leading course content providers.
Our highly qualified academic staff, HUGE resource library of up to date courses and cutting edge white label LMS enable our affiliates to stay well ahead of their competitors
A section for 'Free information pack' like the one on https://www.studyharbour.online/
Target Market(s)
Education providers looking to licence our courses to sell
Number of Pages Required
1 page

```html
<!DOCTYPE html>
<html lang="en">
<head>
<meta charset="utf-8">
<title>BRV Remote Learning – Affiliate Program</title>
<link href="https://fonts.googleapis.com/css2?family=Cinzel:wght@400;600;700&family=Roboto+Condensed:wght@400&family=Mulish:wght@400;600&display=swap" rel="stylesheet">
<style>
:root{
  --navy:#054560;
  --navy-dark:#043a52;
  --gold:#f0bd4f;
  --gold-text:#e9b64a;
  --coral:#f05c58;
  --coral-text:#ee5a55;
  --ink:#3a3a3a;
  --muted:#555;
  --white:#fff;
  --line:#f7c2c0;
}
*{margin:0;padding:0;box-sizing:border-box}
html,body{width:1200px;height:3990px;overflow:hidden;background:var(--white)}
body{font-family:"Mulish",sans-serif;color:var(--ink);position:relative}
.abs{position:absolute}
.sc{font-family:"Cinzel",serif;font-variant:small-caps}
.btn{position:absolute;display:flex;align-items:center;justify-content:center;font-family:"Cinzel",serif;font-size:18px;letter-spacing:.5px}
.btn-navy{background:var(--navy);color:var(--gold-text)}
.btn-gold{background:var(--gold);color:var(--navy)}
.photo{position:absolute}

/* header */
.site-header{position:absolute;left:0;top:0;width:1200px;height:98px}
.brand-name{position:absolute;left:142px;top:10px;font-family:"Cinzel",serif;font-size:14px;color:var(--navy);border-bottom:1px solid var(--navy);padding-bottom:1px}
.brand-mark{position:absolute;left:332px;top:12px;width:20px;height:20px;border:1px solid var(--navy)}
.brand-tag{position:absolute;left:142px;top:57px;width:222px;height:25px;background:var(--navy);color:var(--gold-text);font-family:"Cinzel",serif;font-size:17px;display:flex;align-items:center;justify-content:center}
.contact-chip{position:absolute;top:12px;display:flex;align-items:center;gap:12px;font-size:14px;color:#222}
.chip-icon{width:30px;height:30px;border-radius:50%;border:1px solid var(--navy);display:flex;align-items:center;justify-content:center}
.main-nav{position:absolute;left:475px;top:63px;display:flex;gap:13px;font-family:"Cinzel",serif;font-size:14px;color:#222}

/* hero */
.hero{position:absolute;left:0;top:98px;width:1200px;height:492px}
.hero-left{left:0;top:0;width:660px;height:492px;background:linear-gradient(90deg,#2c2c2a,#55544e 60%,#8a877d)}
.hero-right{left:660px;top:0;width:540px;height:492px;background:linear-gradient(100deg,#d8d4cc,#c9bfb2 45%,#9fa6b2)}
.hero-title{position:absolute;left:144px;top:115px;font-family:"Roboto Condensed",sans-serif;font-size:62px;line-height:66px;color:var(--white)}
.hero-title .accent{color:var(--coral)}
.hero-title .boxed{display:inline-block;background:var(--gold);color:var(--navy);padding:0 10px;margin-left:-3px;margin-top:10px;line-height:56px}
.hero .btn{left:142px;top:343px;width:152px;height:39px}

/* intro */
.intro-heading{position:absolute;left:0;top:680px;width:1200px;text-align:center;font-family:"Cinzel",serif;font-size:30px;line-height:46px;color:var(--navy)}
.intro-pitch{position:absolute;left:152px;top:862px;width:420px;font-family:"Cinzel",serif;font-size:30px;line-height:45px;color:var(--coral-text)}
.video-accent{position:absolute;left:692px;top:859px;width:367px;height:245px;background:var(--gold);clip-path:polygon(100% 0,100% 100%,0 100%,10% 94%,94% 94%,94% 4%)}
.video-thumb{left:635px;top:796px;width:410px;height:294px;background:linear-gradient(135deg,#7a7a7a,#6b6b6b)}

/* lms */
.lms-band{position:absolute;left:0;top:1197px;width:1200px;height:424px;background:var(--navy)}
.lms-heading{position:absolute;left:0;top:1278px;width:1200px;text-align:center;font-family:"Cinzel",serif;font-size:30px;color:var(--gold-text)}
.lms-copy{position:absolute;left:165px;top:1340px;width:870px;text-align:center;font-size:13.5px;line-height:22px;color:var(--white)}
.lms-video{left:276px;top:1429px;width:648px;height:362px;background:linear-gradient(90deg,#f4f4f4,#eaeaea)}
.play{position:absolute;left:544px;top:1568px;width:112px;height:64px;background:var(--coral);border-radius:6px}
.play::after{content:"";position:absolute;left:46px;top:20px;border-left:22px solid var(--white);border-top:12px solid transparent;border-bottom:12px solid transparent}
.player-bar{position:absolute;left:284px;top:1762px;width:640px;height:22px;background:rgba(30,30,30,.85)}
.player-side{position:absolute;left:896px;top:1437px;display:flex;flex-direction:column;gap:6px}
.player-side span{display:block;width:24px;height:24px;background:rgba(30,30,30,.85)}

/* about */
.about-photo{left:0;top:1887px;width:599px;height:480px;background:linear-gradient(120deg,#6b6a5c,#b7b3a5 50%,#e7e3da)}
.about-heading{position:absolute;left:635px;top:1937px;font-family:"Cinzel",serif;font-size:31px;line-height:45px;color:var(--navy)}
.about-copy{position:absolute;left:639px;top:2032px;width:440px;font-size:14.5px;line-height:25px;color:var(--muted)}
.about-copy p{margin-bottom:6px}
.about-btn{left:639px;top:2255px;width:216px;height:42px}

/* info pack */
.info-panel{position:absolute;left:599px;top:2368px;width:601px;height:449px;background:var(--coral)}
.info-heading{position:absolute;left:142px;top:2460px;font-family:"Cinzel",serif;font-size:31px;color:var(--navy)}
.info-sub{position:absolute;left:140px;top:2520px;font-size:20px;color:#333}
.info-q{position:absolute;left:142px;top:2568px;font-size:20px;color:#333}
.info-list{position:absolute;left:161px;top:2611px;font-size:14.5px;line-height:31px;color:#444}
.field{position:absolute;left:647px;width:384px;border-bottom:1px solid var(--line);color:var(--white);font-size:12px;display:flex;align-items:flex-end;gap:14px;padding-bottom:3px}
.field svg{flex:none;margin-bottom:4px}
.submit{left:647px;top:2680px;width:119px;height:41px}

/* difference */
.diff-photo{left:0;top:2817px;width:599px;height:451px;background:linear-gradient(100deg,#8b8a6e,#c7b89a 45%,#e6e0d6)}
.diff-heading{position:absolute;left:641px;top:2922px;font-family:"Cinzel",serif;font-size:31px;color:var(--navy)}
.diff-list{position:absolute;left:658px;top:2975px;font-size:14.5px;line-height:25px;color:#444}
.diff-contact{position:absolute;left:642px;top:3095px;font-size:20px;line-height:34px;color:#333}
.diff-contact .tel{color:var(--coral-text)}

/* cta */
.cta-heading{position:absolute;left:0;top:3348px;width:1200px;text-align:center;font-family:"Cinzel",serif;font-size:29px;color:var(--navy)}
.cta-copy{position:absolute;left:0;top:3391px;width:1200px;text-align:center;font-size:20px;line-height:34px;color:#333}
.cta-btn{left:491px;top:3469px;width:216px;height:42px}

/* footer */
.site-footer{position:absolute;left:0;top:3602px;width:1200px;height:388px;background:var(--navy);color:var(--white)}
.foot-box{position:absolute;top:81px;width:212px;height:153px;border:1px solid #2d6b85;text-align:center}
.foot-box svg{margin-top:26px}
.foot-box .label{font-family:"Cinzel",serif;font-size:17px;margin-top:10px}
.foot-box .val{font-size:13.5px;margin-top:2px}
.foot-brand{position:absolute;left:474px;top:122px;width:252px;text-align:center}
.foot-brand .name{font-family:"Cinzel",serif;font-size:17px;border-bottom:1px solid var(--white);display:inline-block;padding-bottom:2px}
.foot-brand .tag{margin-top:10px;height:26px;background:var(--gold);color:var(--navy);font-family:"Cinzel",serif;font-size:18px;display:flex;align-items:center;justify-content:center}
.foot-nav{position:absolute;top:280px;left:0;width:1200px;display:flex;justify-content:center;gap:34px;font-family:"Cinzel",serif;font-size:15px}
.foot-rule{position:absolute;left:142px;top:314px;width:916px;height:1px;background:#2d6b85}
.copyright{position:absolute;top:333px;left:0;width:1200px;text-align:center;font-family:"Cinzel",serif;font-size:12px}
</style>
</head>
<body>

<header class="site-header">
  <div class="brand-name">BRV Remote Learning</div>
  <div class="brand-mark"></div>
  <div class="brand-tag">Affiliate Program</div>
  <div class="contact-chip" style="left:698px">
    <span class="chip-icon"><svg width="14" height="14" viewBox="0 0 24 24" fill="none" stroke="#054560" stroke-width="2"><path d="M5 3h4l2 5-3 2a11 11 0 0 0 6 6l2-3 5 2v4a2 2 0 0 1-2 2A17 17 0 0 1 3 5a2 2 0 0 1 2-2z"/></svg></span>555.201.4470
  </div>
  <div class="contact-chip" style="left:862px">
    <span class="chip-icon"><svg width="14" height="14" viewBox="0 0 24 24" fill="none" stroke="#054560" stroke-width="2"><rect x="3" y="5" width="18" height="14"/><path d="M3 5l9 8 9-8"/></svg></span>hello@brvpartnerhub.com
  </div>
  <nav class="main-nav"><span>About us</span><span>Our Courses</span><span>LMS Platform</span><span>Affiliate Program</span><span>Contact Us</span></nav>
</header>

<section class="hero">
  <div class="photo hero-left" role="img" aria-label="Dim modern cafe interior with tables and potted plants"></div>
  <div class="photo hero-right" role="img" aria-label="Smiling student sitting cross-legged with a laptop in a bright room"></div>
  <h1 class="hero-title">Start Your <span class="accent">Own</span><br>Distance Education<br><span class="boxed">Business</span></h1>
  <div class="btn btn-navy">Learn More</div>
</section>

<h2 class="intro-heading">Over 450 courses written by highly qualified<br>academics with real world experiencev</h2>
<p class="intro-pitch">The ‘Join our thriving group of Affiliates - start your own online college!’</p>
<div class="video-accent"></div>
<div class="photo video-thumb" role="img" aria-label="Becoming an Affiliate video thumbnail with city skyline sketch"></div>

<section class="lms-band"></section>
<h2 class="lms-heading">See How Our LMS Works</h2>
<p class="lms-copy">lorem ipsum dolor sit amet, consectetuer adipiscing elit, sed diam nonummy nibh euismod tincidunt ut laoreet dolore magna aliquam erat volutpat. ut wisi enim ad minim veniam, quis nostrud exerci tation ullamcorper suscipit lobortis nisl ut aliquip ex ea commodo consequat. duis autem vel eum iriure dolor in hendrerit in vulputate velit.</p>
<div class="photo lms-video" role="img" aria-label="Become an agent video still showing an illustrated person working at a desk"></div>
<div class="player-side"><span></span><span></span><span></span></div>
<div class="play"></div>
<div class="player-bar"></div>

<div class="photo about-photo" role="img" aria-label="Woman working on a laptop by a window"></div>
<h2 class="about-heading">About<br>BRV Remote Learning</h2>
<div class="about-copy">
  <p>BRV Remote Learning has been providing distance education for over 40 years and have been the leader in online education for over 25 years.</p>
  <p>Benefit from the resources and experience of one of the worlds leading course content providers.</p>
  <p>Our highly qualified academic staff, HUGE resource library of up to date courses &amp; cutting edge white label LMS enable our affiliates to stay well ahead of their competitors.</p>
</div>
<div class="btn btn-navy about-btn">Contact Us Today</div>

<div class="info-panel"></div>
<h2 class="info-heading">Free Information Pack</h2>
<p class="info-sub">Get Free Access To Our Info Packs</p>
<p class="info-q">What’s in the info packs?</p>
<ul class="info-list">
  <li>Full list of available course learning resources</li>
  <li>Complete how it works guide</li>
  <li>Latest offers and special promos</li>
  <li>Frequently asked questions</li>
</ul>
<div class="field" style="top:2456px;height:28px"><svg width="14" height="16" viewBox="0 0 24 24" fill="none" stroke="#fff" stroke-width="2"><circle cx="12" cy="8" r="4"/><path d="M4 22a8 8 0 0 1 16 0"/></svg>First Name</div>
<div class="field" style="top:2507px;height:28px"><svg width="16" height="12" viewBox="0 0 24 18" fill="none" stroke="#fff" stroke-width="2"><rect x="1" y="1" width="22" height="16"/><path d="M1 1l11 9 11-9"/></svg>Email</div>
<div class="field" style="top:2557px;height:28px"><svg width="15" height="15" viewBox="0 0 24 24" fill="none" stroke="#fff" stroke-width="2"><path d="M4 20h4L20 8l-4-4L4 16z"/></svg>Send me an info pack &amp; course list information</div>
<div class="field" style="top:2600px;height:62px;align-items:flex-start;padding-top:8px"><svg width="15" height="15" viewBox="0 0 24 24" fill="none" stroke="#fff" stroke-width="2"><path d="M3 4h18v12H8l-5 4z"/></svg>Message</div>
<div class="btn btn-navy submit">Submit</div>

<div class="photo diff-photo" role="img" aria-label="Woman relaxing in an armchair with a mug beside a laptop"></div>
<h2 class="diff-heading">How are we different?</h2>
<ul class="diff-list">
  <li>No Set Up Costs</li>
  <li>No Fixed Costs</li>
  <li>Pay For Content As You Use It</li>
  <li>True Plug And Play Solution</li>
</ul>
<p class="diff-contact">Speak to our team today on <span class="tel">555.201.4470</span><br>or email hello@brvpartnerhub.com</p>

<h2 class="cta-heading">Interested in becoming an affiliate?</h2>
<p class="cta-copy">Contact us now to discuss how we can work together to launch your own<br>Distance Education Business...</p>
<div class="btn btn-gold cta-btn">Contact Us Today</div>

<footer class="site-footer">
  <div class="foot-box" style="left:189px">
    <svg width="40" height="34" viewBox="0 0 40 34" fill="none" stroke="#f0bd4f" stroke-width="2"><rect x="2" y="6" width="36" height="26"/><path d="M2 6l18 15L38 6"/></svg>
    <div class="label sc">Email</div>
    <div class="val">hello@brvpartnerhub.com</div>
  </div>
  <div class="foot-brand">
    <div class="name">BRV Remote Learning</div>
    <div class="tag">Affiliate Program</div>
  </div>
  <div class="foot-box" style="left:797px">
    <svg width="38" height="38" viewBox="0 0 24 24" fill="none" stroke="#f0bd4f" stroke-width="1.5"><path d="M5 3h4l2 5-3 2a11 11 0 0 0 6 6l2-3 5 2v4a2 2 0 0 1-2 2A17 17 0 0 1 3 5a2 2 0 0 1 2-2z"/></svg>
    <div class="label sc">Phone</div>
    <div class="val">555.201.4470</div>
  </div>
  <nav class="foot-nav"><span>About us</span><span>Our Courses</span><span>LMS Platform</span><span>Affiliate Program</span><span>Contact Us</span></nav>
  <div class="foot-rule"></div>
  <p class="copyright">© 2021 BRV Remote Learning. All Rights Reserved.</p>
</footer>

</body>
</html>
```